Business card design for sports medicine and athlete care clinic.

We need a bold, solid business card design for our practitioners to stand out. We treat overuse & sports-related injuries and provide post-operative rehabilitation. Our specialisations include chronic conditions, men’s health, nutrition & musculoskeletal disorders (MSDs). All brand collateral in terms of fonts, logo and colour palette to be provided.

Target Market(s)

Athletes (professional and amateur), sportspeople, predominantly male

Industry/Entity Type

Health And Wellness

Contact Information for Business Card

The front of the card should be white with dark blue text the back dark blue with white text. The logo should be top-left. The business name should be horizontal and right of the logo. The tagline should be directly below centred on the back of the card (see top-banner.png and bottom-banner.png)

Font styles to use
Sans Serif

Colors
0355a3
0293ce
3176b5
ffffff
85acd3

Requirements
Nice to have
• Diagonal and/or horizontal line elements between logo and practitioner details and/or bottom corner of card (see slide.png and tag-bg.png).

```html
<!DOCTYPE html>
<html lang="en">
<head>
<meta charset="utf-8">
<title>The Stride Clinic – Business Card</title>
<link rel="stylesheet" href="https://fonts.googleapis.com/css2?family=Roboto:wght@400;500;700&family=Nunito:ital,wght@0,800;1,600&display=swap">
<style>
  :root {
    --backdrop: #8a8a8a;
    --navy: #081d5c;
    --sky: #0293ce;
    --bright: #33a8e6;
    --mid: #1a85c7;
    --pale: #85acd3;
    --charcoal: #444446;
    --white: #ffffff;
    --paper-light: #f4f5f6;
    --paper-dark: #c9cbcd;
  }
  html, body {
    margin: 0;
    width: 1200px;
    height: 801px;
    overflow: hidden;
    background: var(--backdrop);
  }
  .canvas {
    position: relative;
    width: 1200px;
    height: 801px;
  }
  .card {
    position: absolute;
    top: 274px;
    width: 443px;
    height: 263px;
    box-shadow: 2px 2px 2px rgba(0,0,0,0.55);
    overflow: hidden;
  }
  .card svg { display: block; width: 443px; height: 263px; }
  .card--details { left: 153px; background: var(--white); }
  .card--brand { left: 625px; }
  .details-text { font-family: 'Roboto', Arial, sans-serif; fill: var(--white); }
  .details-name { font-weight: 700; font-size: 28px; }
  .details-line { font-size: 21px; }
  .brand-name { font-family: 'Nunito', Arial, sans-serif; font-weight: 800; font-size: 37px; fill: var(--navy); }
  .brand-tagline { font-family: 'Nunito', Arial, sans-serif; font-style: italic; font-weight: 600; font-size: 22px; fill: var(--sky); }
  .brand-handle { font-family: 'Roboto', Arial, sans-serif; font-size: 22px; fill: var(--white); }
</style>
</head>
<body>
<div class="canvas">

  <!-- Practitioner details side -->
  <div class="card card--details">
    <svg viewBox="0 0 738 439" xmlns="http://www.w3.org/2000/svg">
      <defs>
        <linearGradient id="illustrationTone" x1="0" y1="1" x2="1" y2="0">
          <stop offset="0" stop-color="#cfe4f3"/>
          <stop offset="1" stop-color="#9cc6e6"/>
        </linearGradient>
      </defs>
      <rect class="details-panel" x="0" y="0" width="738" height="439" fill="var(--navy)"/>
      <polygon class="illustration-area" role="img"
               aria-label="Illustration of a sprinter in motion, in layered blue tones"
               fill="url(#illustrationTone)"
               points="0,0 490,0 490,190 340,300 340,439 0,439"/>

      <g class="details-text" text-anchor="end">
        <text class="details-name" x="695" y="226">DANIEL REYES</text>
        <text class="details-line" x="692" y="251">Managing Director</text>
        <text class="details-line" x="664" y="288">044-555 010 247</text>
        <text class="details-line" x="664" y="314">hello@stride.com</text>
        <text class="details-line" x="664" y="341">www.stride.com</text>
        <text class="details-line" x="695" y="376">88, Harbour Road East Side</text>
        <text class="details-line" x="695" y="402">30214, Australia</text>
      </g>

      <g class="contact-icons">
        <circle cx="684" cy="281" r="11" fill="var(--white)"/>
        <path d="M679,275 l3,-1 l2,4 l-2,1.5 q1.5,3.5 4.5,4.5 l1.5,-2 l4,2 l-1,3 q-8,0 -12,-12 z" fill="var(--navy)"/>
        <circle cx="684" cy="307" r="11" fill="var(--white)"/>
        <rect x="677" y="302" width="14" height="10" fill="none" stroke="var(--navy)" stroke-width="1.6"/>
        <path d="M677,302 l7,6 l7,-6" fill="none" stroke="var(--navy)" stroke-width="1.6"/>
        <circle cx="684" cy="334" r="11" fill="var(--white)"/>
        <circle cx="684" cy="334" r="7" fill="none" stroke="var(--navy)" stroke-width="1.5"/>
        <ellipse cx="684" cy="334" rx="3" ry="7" fill="none" stroke="var(--navy)" stroke-width="1.3"/>
        <line x1="677" y1="334" x2="691" y2="334" stroke="var(--navy)" stroke-width="1.3"/>
      </g>
    </svg>
  </div>

  <!-- Brand side -->
  <div class="card card--brand">
    <svg viewBox="0 0 738 439" xmlns="http://www.w3.org/2000/svg">
      <defs>
        <radialGradient id="paperTone" cx="0.72" cy="0.3" r="0.85">
          <stop offset="0" stop-color="var(--paper-light)"/>
          <stop offset="0.55" stop-color="#e3e4e6"/>
          <stop offset="1" stop-color="var(--paper-dark)"/>
        </radialGradient>
      </defs>
      <rect width="738" height="439" fill="url(#paperTone)"/>

      <polygon class="stripe stripe--charcoal" fill="var(--charcoal)"
               points="40,0 66,0 28,165 236,439 168,439 0,172 0,150"/>
      <polygon class="stripe stripe--bright" fill="var(--bright)"
               points="74,0 96,0 54,178 30,168"/>
      <polygon class="stripe stripe--mid" fill="var(--mid)"
               points="54,178 325,439 236,439 30,168"/>

      <polygon class="social-band" fill="var(--navy)" points="238,341 738,341 738,397 295,397"/>
      <circle cx="426" cy="366" r="11" fill="var(--white)"/>
      <text class="brand-handle" x="478" y="373">StrideClinicAU</text>

      <circle class="brand-mark" cx="232" cy="150" r="34" fill="var(--sky)"/>
      <text class="brand-name" x="313" y="142">The Stride Clinic</text>
      <text class="brand-tagline" x="315" y="166">Sports medicine and athlete care</text>
    </svg>
  </div>

</div>
</body>
</html>
```